依頼詳細
主な参加者は女性になりますので、女性的なデザインでお願いします。バナー制作ですが、ポスターのように縦長サイズのイメージになります。
記載項目
バナーに記載していただきたい内容は以下のとおりです。

---ここから---

2月4日は『妊娠の日』
業界初!マタニティヨガインストラクターと鍼灸師がコラボ!
妊活体操イベント開催

<妊活体操イベント概要>
開催日時:2017年2月4日(土)13:00~14:00
*館内着に着替えるため、余裕をもって30分以上前のご来場をお願いいたします。
開催場所:SPA ORIN(神奈川県横浜市西区南空3-5-7 ソラモールクレオ内)

◆当日のプログラム内容
⑴ご挨拶・趣旨説明
⑵マタニティヨガの話・葉酸の話・にんかツボの話
⑶妊活体操
⑷質疑応答

参加費:3,000円(入館料2,880円を含む)
定員:30名(カップルでのご来場もお待ちしております。)
備考:イベント終了後はSPA ORIN内の施設をご利用いただけます。
(深夜3時以降は別途1,730円の利用料が必要です。)

---ここまで---

妊活体操をイメージできるような画像の使用をお願いいたします。
(後日、こちらで撮影した写真に差し替えを行います。)

なお、イベントの会場はこちらになります。
http://www.spa-orin-web.jp/

イベントの告知・集客はこちらのサイトで行います。
http://mirefolle.com/
サイズ
• 横768px(縦は自由です)
希望イメージ
シンプル 複雑
単色 カラフル
暗い 明るい
日常 高級
遊び心 厳粛
未来的 伝統的
女性的 男性的
希望する色
赤系、茶系、妊活ですのでピンク系を使っていただくようお願いいたします。
納品ファイル
• 高解像度JPG (.jpg)
補足説明
◆コンペ参加条件
・1/16に本イベントに関する撮影を行いますので、イメージ写真の差し替え対応までできる方(今回のコンペ費用に含みます。)
・今後定期的にイベントを開催する方向で検討しておりますので、その際は開催日時や開催場所の修正対応をお願いできる方(こちらは別途2,000円/回の費用をお支払いします。手数料込、税別)
弊社スケジュールの都合により、締切を1/5に変更させていただきます。
ご提案どうぞよろしくお願いいたします。

必要な情報が一番目立つようにレイアウトされており、その他の情報もスッキリと分かりやすく書かれていることで、パソコンでみてもスマホでみても視認性が高かった点を評価させていただきました。女性的な雰囲気もイメージどおりでした。

今回は多数の素敵な提案をいただき感謝しております。どうもありがとうございました。

```html
<!DOCTYPE html>
<html lang="ja">
<head>
<meta charset="utf-8">
<title>妊活体操イベント開催</title>
<link rel="stylesheet" href="https://fonts.googleapis.com/css2?family=M+PLUS+Rounded+1c:wght@400;700;800;900&display=swap">
<style>
:root{
  --pink-bg:#f9d3e0;
  --pink-light:#fde8ef;
  --pink:#ee5a95;
  --pink-deep:#e23d7d;
  --magenta:#d81b6f;
  --purple:#7a2f8e;
  --red:#e5262d;
  --brown:#6b3a2a;
  --cream:#fffaf3;
  --white:#ffffff;
  --text:#3b2a2a;
}
*{margin:0;padding:0;box-sizing:border-box}
html,body{width:1200px;height:2184px;overflow:hidden}
body{font-family:"M PLUS Rounded 1c",sans-serif;color:var(--text);background:var(--white)}
.banner{position:relative;width:1200px;height:2184px;overflow:hidden;
  background:radial-gradient(circle at 30% 20%,#fff3f7 0,var(--pink-bg) 55%,#f4b9cf 100%)}
.abs{position:absolute}

.belly-photo{right:0;top:0;width:400px;height:440px;border-radius:0 0 0 60%;
  background:radial-gradient(circle at 60% 45%,#fbe4dc 0,#f2c4b4 50%,#f7d9e4 100%)}

.date-ribbon{left:340px;top:0;width:540px;height:84px;background:linear-gradient(var(--pink),var(--pink-deep));
  border-radius:0 0 24px 24px;display:flex;align-items:center;justify-content:center;
  color:var(--white);font-weight:900;font-size:48px;letter-spacing:2px;box-shadow:0 4px 8px rgba(160,30,80,.3)}
.date-ribbon .heart{color:#ffd6e6;margin:0 10px;font-size:38px}

.first-badge{left:190px;top:200px;width:150px;height:150px;border-radius:50%;
  background:radial-gradient(circle at 35% 30%,#ff5a5f,var(--red));border:6px solid var(--white);
  color:var(--white);font-weight:900;font-size:36px;line-height:1.1;display:flex;align-items:center;justify-content:center;text-align:center;
  transform:rotate(-12deg);box-shadow:0 4px 10px rgba(150,0,0,.25)}

.collab{top:100px;color:var(--purple);font-weight:900;font-size:56px;line-height:1.2;white-space:nowrap;
  text-shadow:4px 4px 0 var(--white),-4px -4px 0 var(--white),4px -4px 0 var(--white),-4px 4px 0 var(--white)}
.collab .l1{display:block;padding-left:80px}
.collab .l3{display:block;padding-left:20px}
.collab{left:360px}

.title{left:0;top:318px;width:1200px;text-align:center;color:var(--pink-deep);font-weight:900;font-size:98px;line-height:1.2;letter-spacing:2px;white-space:nowrap;
  text-shadow:6px 6px 0 var(--white),-6px -6px 0 var(--white),6px -6px 0 var(--white),-6px 4px 0 var(--white),0 8px 12px rgba(160,30,80,.35)}

.pose-photo{left:0;top:740px;width:1200px;height:640px;
  background:linear-gradient(180deg,#fdf3f6 0,#f8dbe5 55%,#f3c5d6 100%)}
.flower-deco{left:940px;top:1300px;width:230px;height:230px;border-radius:50%;
  background:radial-gradient(circle,#fbd4e2 0,#ef9fbe 60%,rgba(240,160,190,0) 72%)}

.overview{left:300px;top:470px;width:860px;height:280px;background:var(--cream);border:6px solid var(--pink);border-radius:14px;
  box-shadow:0 4px 10px rgba(160,30,80,.2)}
.overview-head{position:absolute;left:0;top:0;width:100%;height:52px;background:var(--pink);color:var(--white);
  font-weight:800;font-size:36px;display:flex;align-items:center;justify-content:center}
.overview-body{padding:62px 30px 0;color:var(--brown)}
.overview-body .row{font-size:38px;font-weight:800;line-height:1.3;white-space:nowrap}
.overview-body .label{color:var(--magenta)}
.overview-body .addr{font-size:23px;font-weight:700;text-align:right;line-height:1.4;white-space:nowrap}
.overview-body .note{font-size:29px;font-weight:700;color:var(--text);margin-top:4px;line-height:1.35;text-align:center}

.program{left:150px;top:1420px;width:960px;height:310px;background:var(--white);border:4px solid var(--pink);border-radius:20px;
  box-shadow:0 4px 10px rgba(160,30,80,.15)}
.program-head{position:absolute;left:250px;top:-30px;width:460px;height:60px;background:var(--pink-light);border:4px solid var(--pink);
  border-radius:30px;color:var(--magenta);font-weight:800;font-size:36px;display:flex;align-items:center;justify-content:center}
.program-list{list-style:none;padding:48px 0 0 110px}
.program-list li{display:flex;align-items:center;font-size:38px;font-weight:800;color:var(--brown);height:60px;white-space:nowrap}
.program-list .num{width:44px;height:44px;border-radius:50%;background:var(--pink-deep);color:var(--white);
  font-size:28px;display:flex;align-items:center;justify-content:center;margin-right:18px;flex:none}
.program-list .small{font-size:32px}

.yoga-photo{left:30px;top:1440px;width:190px;height:190px;border-radius:50%;border:6px solid var(--white);
  background:radial-gradient(circle,#f7d3b8 0,#e8a97f 60%,#f0c7a8 100%)}

.info-box{top:1752px;height:330px;border-radius:16px;background:var(--white);border:5px solid var(--pink);text-align:center}
.fee{left:20px;width:370px}
.facility{left:412px;width:376px;background:var(--pink-light)}
.capacity{left:810px;width:370px}
.info-label{display:inline-block;margin-top:30px;background:var(--pink-deep);color:var(--white);font-weight:800;font-size:38px;
  padding:4px 22px;border-radius:8px}
.info-big{color:var(--red);font-weight:900;font-size:92px;line-height:1.15}
.info-big small{font-size:46px}
.info-sub{font-size:27px;font-weight:700;color:var(--brown)}
.facility p{font-size:34px;font-weight:800;color:var(--brown);line-height:1.5;margin-top:48px}
.facility .hl{color:var(--magenta)}

.footer{left:0;top:2098px;width:1200px;height:86px;background:var(--pink-deep);color:var(--white);
  font-weight:800;font-size:40px;display:flex;align-items:center;justify-content:center;letter-spacing:1px}
</style>
</head>
<body>
<div class="banner">
  <div class="abs belly-photo" role="img" aria-label="妊婦のおなかに手でハートを作った写真"></div>
  <div class="abs pose-photo" role="img" aria-label="ヨガマットの上でブリッジのポーズをとる女性の写真"></div>
  <div class="abs flower-deco" role="img" aria-label="ピンクの花と小物の飾り"></div>

  <div class="abs date-ribbon">2月4日は<span class="heart">♥</span>妊娠の日</div>
  <div class="abs collab"><span class="l1">マタニティ</span>ヨガインストラクターと<span class="l3">鍼灸師がコラボ!</span></div>
  <div class="abs first-badge">業界<br>初!</div>
  <h1 class="abs title">妊活体操イベント開催</h1>

  <section class="abs overview">
    <div class="overview-head">妊活体操イベント概要</div>
    <div class="overview-body">
      <div class="row"><span class="label">開催日時：</span>2017/2/4（土）13:00 ~ 14:00</div>
      <div class="row"><span class="label">開催場所：</span>SPA ORIN</div>
      <div class="addr">（神奈川県横浜市西区南空3-5-7 ソラモールクレオ内）</div>
      <div class="note">＊館内着に着替えるため、余裕をもって<br>30分以上前のご来場をお願いいたします。</div>
    </div>
  </section>

  <section class="abs program">
    <div class="program-head">当日のプログラム内容</div>
    <ol class="program-list">
      <li><span class="num">1</span>ご挨拶・趣旨説明</li>
      <li><span class="num">2</span><span class="small">マタニティヨガの話・葉酸の話・にんかツボの話</span></li>
      <li><span class="num">3</span>妊活体操</li>
      <li><span class="num">4</span>質疑応答</li>
    </ol>
  </section>
  <div class="abs yoga-photo" role="img" aria-label="ヨガのポーズをとる女性の写真"></div>

  <div class="abs info-box fee">
    <span class="info-label">参加費</span>
    <div class="info-big">3,000<small>円</small></div>
    <div class="info-sub">入館料2,880円を含む</div>
  </div>
  <div class="abs info-box facility">
    <p>イベント終了後は<br><span class="hl">SPA ORIN</span>内の施設を<br>ご利用いただけます</p>
  </div>
  <div class="abs info-box capacity">
    <span class="info-label">定員</span>
    <div class="info-big">30<small>名</small></div>
    <div class="info-sub">カップルでのご来場も<br>お待ちしております</div>
  </div>

  <div class="abs footer">深夜3時以降は別途1,730円の利用料が必要です。</div>
</div>
</body>
</html>
```